1923 Basins & Spouts Business Card

I'm wanting to get a business card designed. Our business is 1923 Basins & Spouts
Details for the card:

1923 Basins & Spouts
Name: Gareth Vostle
Email: gareth@1923basinsandspouts.com.au
Website: www.1923basinsandspouts.com.au
Mobile: 0439 602 158
Phone: 02 5550 1843

Font of Basins & Spouts is called Snell Roundhand. Not sue what font logo text is.

I'm thinking two sided but it doesn't have to be.

```html
<!DOCTYPE html>
<html lang="en">
<head>
<meta charset="utf-8">
<title>1923 Basins &amp; Spouts – Business Card</title>
<link href="https://fonts.googleapis.com/css2?family=Lato:wght@400;700&family=Arimo:wght@700&display=swap" rel="stylesheet">
<style>
  :root {
    --backdrop: #2b2d30;
    --card-black: #0b0b0c;
    --card-white: #ffffff;
    --band-grey: #606060;
    --ink-light: #ffffff;
    --ink-dark: #111111;
  }
  * { box-sizing: border-box; margin: 0; padding: 0; }
  html, body { width: 1200px; height: 1000px; overflow: hidden; }
  body {
    background: var(--backdrop);
    font-family: "Lato", sans-serif;
    position: relative;
  }
  .card {
    position: absolute;
    left: 250px;
    width: 700px;
    height: 400px;
    border-radius: 22px;
    overflow: hidden;
  }
  .card--back { top: 60px; background: var(--card-black); color: var(--ink-light); }
  .card--front { top: 540px; background: var(--card-white); }

  .brand { position: absolute; display: flex; align-items: center; gap: 16px; }
  .brand__mark { width: 62px; height: 62px; border-radius: 50%; border: 2px solid currentColor; flex: none; }
  .brand__name { font-size: 26px; font-weight: 400; white-space: nowrap; }
  .brand__tagline { position: absolute; font-size: 12.5px; letter-spacing: 0.2px; white-space: nowrap; }

  .card--back .brand { left: 190px; top: 135px; }
  .card--back .brand__tagline { left: 268px; top: 212px; }
  .card--back .company-line {
    position: absolute; left: 0; right: 0; top: 318px;
    text-align: center; font-size: 17px;
  }

  .wave { position: absolute; inset: 0; width: 700px; height: 400px; }

  .card--front .brand { left: 345px; top: 72px; color: var(--ink-dark); }
  .card--front .brand__name { font-size: 22px; }
  .card--front .brand__tagline { left: 395px; top: 146px; color: var(--ink-dark); font-size: 11.5px; }

  .person {
    position: absolute; left: 40px; top: 148px;
    font-family: "Arimo", sans-serif; font-weight: 700;
    font-size: 26px; color: var(--ink-light); letter-spacing: 0.5px;
  }
  .contacts { position: absolute; left: 40px; top: 196px; list-style: none; color: var(--ink-light); }
  .contacts li { display: flex; align-items: center; gap: 10px; font-size: 17px; height: 27px; }
  .contacts svg { width: 14px; height: 14px; flex: none; }
  .address {
    position: absolute; right: 40px; top: 322px;
    text-align: right; font-size: 18px; line-height: 1.3; color: var(--ink-light);
    font-style: normal;
  }
</style>
</head>
<body>

<section class="card card--back">
  <div class="brand">
    <span class="brand__mark"></span>
    <span class="brand__name">1923 Basins &amp; Spouts</span>
  </div>
  <p class="brand__tagline">Combining timeless beauty with perfect practicality</p>
  <p class="company-line">1923 Basins &amp; Spouts</p>
</section>

<section class="card card--front">
  <svg class="wave" viewBox="0 0 700 400" aria-hidden="true">
    <path fill="var(--band-grey)" d="M0,92 C180,84 300,136 390,214 C470,282 580,290 700,280 L700,400 L0,400 Z"/>
    <path fill="var(--card-white)" d="M0,103 C180,95 300,147 390,225 C470,293 580,301 700,291 L700,400 L0,400 Z"/>
    <path fill="var(--card-black)" d="M0,109 C180,101 300,153 390,231 C470,299 580,307 700,297 L700,400 L0,400 Z"/>
  </svg>

  <div class="brand">
    <span class="brand__mark"></span>
    <span class="brand__name">1923 Basins &amp; Spouts</span>
  </div>
  <p class="brand__tagline">Combining timeless beauty with perfect practicality</p>

  <h1 class="person">Gareth Vostle</h1>
  <ul class="contacts">
    <li>
      <svg viewBox="0 0 16 16"><path fill="#fff" d="M3.5 1l2.5 3-1.5 1.8c.8 1.8 2 3 3.8 3.8L10 8l3 2.5-1.5 2.5C6 13 3 10 2 3.5z"/></svg>
      02 5550 1843
    </li>
    <li>
      <svg viewBox="0 0 16 16"><rect x="4" y="1" width="8" height="14" rx="1.5" fill="none" stroke="#fff" stroke-width="1.6"/><circle cx="8" cy="12.3" r="0.9" fill="#fff"/></svg>
      0439 602 158
    </li>
    <li>
      <svg viewBox="0 0 16 16"><rect x="1" y="3" width="14" height="10" fill="#fff"/><path d="M1 3l7 6 7-6" fill="none" stroke="#0b0b0c" stroke-width="1.4"/></svg>
      gareth@1923basinsandspouts.com.au
    </li>
    <li>
      <svg viewBox="0 0 16 16"><circle cx="8" cy="8" r="6.5" fill="none" stroke="#fff" stroke-width="1.4"/><path d="M1.5 8h13M8 1.5c-3 3-3 10 0 13M8 1.5c3 3 3 10 0 13" fill="none" stroke="#fff" stroke-width="1.1"/></svg>
      www.1923basinsandspouts.com.au
    </li>
  </ul>

  <address class="address">
    Larkfield Crossing, Marrowby<br>
    Ashdene Vale, 1734
  </address>
</section>

</body>
</html>
```